Independent Statistical Consultant Business Card

I will be going out as an independent statistical consultant and need a business card. I specialize in data analysis and statistics for health care and public health

I am an Chartered Numeric Analyst from the Northern Quantitative Society. Would like to incorporate that logo into the design

The design should be modern with classic colors, convey accuracy, analytic creativity and responsiveness to client needs.
Updates

The name of the firm will be simply Dale Venturo Applied Statistical Consulting

To all designers, I want to clarify that the QCert logo and the phrase Chartered Numeric Analyst are not the name of the company nor the focus of the card. They are equivalent to being a Lumetra Licensed Technician (LLT) but in the area of statistics The name of the firm will be: Dale Venturo, Applied Statistical Consulting. I look forward to your submissions. Thanks. Dale

Industry/Entity Type

Health

```html
<!DOCTYPE html>
<html lang="en">
<head>
<meta charset="utf-8">
<title>Dale Venturo, Applied Statistical Consulting – Business Card</title>
<link rel="stylesheet" href="https://fonts.googleapis.com/css2?family=Lato:wght@400;700;900&display=swap">
<style>
  :root {
    --backdrop: #2b2b2d;
    --panel-blue: #2a60ad;
    --panel-blue-deep: #1e4e95;
    --card-light: #f1f1f1;
    --card-shade: #dcdcdc;
    --ink-dark: #2a2a2c;
    --ink-grey: #55575c;
    --ink-navy: #0f2547;
    --ink-white: #ffffff;
    --ink-soft: #d7deea;
  }
  * { box-sizing: border-box; margin: 0; padding: 0; }
  html, body {
    width: 1200px;
    height: 1116px;
    overflow: hidden;
    background: var(--backdrop);
    font-family: "Lato", Arial, sans-serif;
  }
  .stage {
    width: 1200px;
    height: 1116px;
    display: flex;
    align-items: center;
    justify-content: center;
  }
  .card {
    width: 960px;
    height: 548px;
    border-radius: 26px;
    overflow: hidden;
    display: flex;
    box-shadow: 0 20px 50px rgba(0,0,0,0.45);
  }
  .contact-panel {
    width: 340px;
    background: linear-gradient(160deg, var(--panel-blue), var(--panel-blue-deep));
    padding: 92px 0 0 56px;
    color: var(--ink-navy);
  }
  .person-name {
    color: var(--ink-white);
    font-weight: 900;
    font-size: 34px;
    letter-spacing: 0.3px;
    white-space: nowrap;
  }
  .person-role {
    font-weight: 700;
    font-size: 15px;
    letter-spacing: 1.4px;
    text-transform: uppercase;
    margin-top: 4px;
  }
  .contact-list {
    list-style: none;
    margin-top: 64px;
  }
  .contact-item {
    display: flex;
    align-items: center;
    gap: 20px;
    font-weight: 700;
    font-size: 18px;
    height: 40px;
    white-space: nowrap;
  }
  .contact-icon {
    width: 22px;
    height: 22px;
    flex: none;
  }
  .contact-icon path, .contact-icon rect {
    fill: none;
    stroke: var(--ink-soft);
    stroke-width: 1.8;
  }
  .office-address {
    color: var(--ink-soft);
    font-weight: 900;
    font-size: 23px;
    line-height: 1.25;
    margin-top: 52px;
    font-style: normal;
  }
  .brand-panel {
    flex: 1;
    background: linear-gradient(135deg, var(--card-light), var(--card-shade));
    display: flex;
    flex-direction: column;
    justify-content: center;
    padding-left: 96px;
    color: var(--ink-dark);
  }
  .firm-name {
    font-weight: 700;
    font-size: 78px;
    line-height: 1;
    letter-spacing: -1px;
    white-space: nowrap;
  }
  .firm-tagline {
    font-weight: 400;
    font-size: 29px;
    margin-top: 12px;
    padding-left: 3px;
    white-space: nowrap;
  }
  .credential {
    display: flex;
    align-items: center;
    gap: 12px;
    margin-top: 40px;
    padding-left: 3px;
    color: var(--ink-grey);
    font-weight: 400;
    font-size: 18px;
    white-space: nowrap;
  }
  .credential-dot {
    width: 12px;
    height: 12px;
    border-radius: 50%;
    background: var(--panel-blue);
    flex: none;
  }
</style>
</head>
<body>
<main class="stage">
  <article class="card">
    <section class="contact-panel">
      <h1 class="person-name">Dale Venturo</h1>
      <p class="person-role">Statistical Consultant</p>
      <ul class="contact-list">
        <li class="contact-item">
          <svg class="contact-icon" viewBox="0 0 24 24" aria-hidden="true"><path d="M3 8c0-2 4-4 9-4s9 2 9 4v2h-5V8H8v2H3z M6 12h12l2 8H4z"/></svg>
          <span>+(555) 0142 7730</span>
        </li>
        <li class="contact-item">
          <svg class="contact-icon" viewBox="0 0 24 24" aria-hidden="true"><rect x="6" y="2" width="12" height="20" rx="2"/><path d="M10 18h4"/></svg>
          <span>+(555) 301 4489</span>
        </li>
        <li class="contact-item">
          <svg class="contact-icon" viewBox="0 0 24 24" aria-hidden="true"><rect x="2" y="5" width="20" height="14" rx="1"/><path d="M2 5l10 8 10-8"/></svg>
          <span>hello@venturostats.com</span>
        </li>
      </ul>
      <address class="office-address">1180 Linden Row,<br>Suite 400, Canada</address>
    </section>
    <section class="brand-panel">
      <div class="firm-name">Dale Venturo</div>
      <div class="firm-tagline">Applied Statistical Consulting</div>
      <div class="credential">
        <span class="credential-dot" aria-hidden="true"></span>
        <span>QCert · Chartered Numeric Analyst</span>
      </div>
    </section>
  </article>
</main>
</body>
</html>
```